Trance Guide Coaching Marketing Materials
Brochure, Postcard, Business Card, Letterhead, Envelope
I've been in non-stop meetings all week, and I apologize for not being quicker with feedback. I'll comment again this evening. Thank you.
I find myself tied up today on other business. I extended the project a couple of days. This will be the only extension. I will choose a winner promptly when the contest closes, as I did with my previous projects. There may be some final tweaking but everything will be completed within a week of closing, no longer than that. I appreciate all your wonderful creative efforts. Thank you, and may you prosper and thrive happily. Kindest regards.
#22 and #8 good but the people shown have no context. The people depicted should be going about their positive activity or business and not necessarily looking directly into the camera.
#23 interesting design but the people are too frenetic, too much energy. Thank you.
Lots of quality work here, everyone. Thank you. Keep on keepin' on. I will review more this evening (EST) and will extend the contest a day or two at least. The entries are very good. I have to be away from my desk the rest of the day, but I will return here later.
#19 try replacing the guy with outstretched arms. He's cool but we should see more ideas in that spot. Play with it.
I'll talk about other designs later today, as indicated in my earlier note. thanks again.
I have a lot to review today. Thank you for your excellent efforts. I may not comment further until this evening, but please keep on keepin' on.
I am considering extending the contest a few days to give everyone time to react to the comments I make later.
Good work, everyone. Thank you.
I meant #6 quite excellent in below comment today (not #4, which was discussed earlier). Sorry for any confusion. Thank you for the effort.
I may have to extend this contest.
#7 I like this, too. Very good, but needs more variety of people. Tricky but that's why you're the designer! Thank you for the effort.
#4 quite excellent. I'm liking it, but it needs something, not sure what. I see 3 out 5 people white, including both women white. Try mixing it up if you can, although I see from a design point of view the poses and angles work. It could be close.
#3 I gave it 3 stars because the designs are good except for the groups of people, which I already talked about. I want to encourage you, though.
Draft #4, the picture of the guy is interesting. I have to sleep on that one.
Draft #3 and #4: About pictures: I'm not looking for groups of people, and I'm not looking for abstract settings. Pictures should feature individuals in typical settings. Examples: business man, business woman, musician, athlete, teacher, sales person. No couples, no groups. Individuals with whom people reading the brochure can identify.
Thank you.
Thank you for your entries. I'll be reviewing entries tomorrow and offering suggestions.
Designers: Logo AI has been uploaded. Please refer to the Creative Brief and proceed. - Dave
Trance Guide Coaching Contact Info
Gordon P Whitfield CLC CCH
4629 Larkmoor Rd Ste 310
Albany NY 12203
phone 518-926-3081
fax 888-547-2263
web http://TranceGuideNow.example

```html
<!DOCTYPE html>
<html lang="en">
<head>
<meta charset="utf-8">
<title>Trance Guide Coaching – Trifold Brochure</title>
<link rel="stylesheet" href="https://fonts.googleapis.com/css2?family=Arimo:ital,wght@0,400;0,700;1,700&display=swap">
<style>
  :root {
    --canvas: #d8d8d8;
    --navy: #1f3a8a;
    --navy-deep: #0c1c4f;
    --green: #8cc63f;
    --grey-text: #6d6f73;
    --white: #ffffff;
  }
  * { box-sizing: border-box; margin: 0; padding: 0; }
  html, body { width: 1200px; height: 957px; overflow: hidden; }
  body { background: var(--canvas); font-family: "Arimo", Arial, sans-serif; position: relative; }

  .brochure {
    position: absolute; left: 85px; top: 86px;
    width: 1030px; height: 785px;
    background: var(--white);
    box-shadow: 0 4px 14px rgba(0,0,0,.25);
    overflow: hidden;
  }
  .brochure-art { position: absolute; inset: 0; width: 1030px; height: 785px; }

  .brand-name { color: var(--navy); font-weight: 700; text-transform: uppercase; line-height: 1; }
  .brand-tagline { color: var(--grey-text); text-transform: uppercase; letter-spacing: .02em; }
  .brand-tagline strong { color: var(--navy); }

  .cover-brand { position: absolute; left: 690px; top: 44px; width: 330px; }
  .cover-brand .brand-name { font-size: 40px; letter-spacing: .01em; }
  .cover-brand .brand-tagline { font-size: 15px; margin-top: 8px; }

  .inside-copy { position: absolute; left: 26px; top: 300px; width: 262px; color: var(--white); }
  .inside-copy h2 { color: var(--green); font-size: 21px; font-weight: 700; margin-bottom: 12px; }
  .inside-copy p { font-size: 11.5px; line-height: 1.42; margin-bottom: 22px; }

  .panel-promise {
    position: absolute; left: 478px; top: 292px; width: 176px;
    text-align: center; color: var(--navy-deep);
    font-weight: 700; font-style: italic; font-size: 23px; line-height: 1.12;
  }

  .contact-panel { position: absolute; left: 372px; top: 538px; width: 250px; text-align: center; color: var(--white); font-style: normal; }
  .contact-panel .brand-name { color: var(--white); font-size: 25px; }
  .contact-panel .brand-tagline { color: var(--green); font-size: 9.5px; margin-top: 4px; }
  .contact-name { color: var(--green); font-weight: 700; font-size: 13.5px; margin-top: 12px; }
  .contact-address { font-size: 12px; line-height: 1.35; margin-top: 5px; }
  .contact-line { margin-top: 8px; font-size: 11px; }
  .contact-line + .contact-line { margin-top: 2px; }
  .contact-line b { font-size: 18px; font-weight: 700; margin-left: 6px; }
  .contact-web { font-weight: 700; font-size: 14px; margin-top: 12px; }
</style>
</head>
<body>
<section class="brochure" aria-label="Trance Guide Coaching trifold brochure">
  <svg class="brochure-art" viewBox="0 0 1030 785" xmlns="http://www.w3.org/2000/svg">
    <defs>
      <linearGradient id="stadiumTones" x1="0" y1="0" x2="0" y2="1">
        <stop offset="0" stop-color="#b8352c"/>
        <stop offset=".45" stop-color="#d06a4d"/>
        <stop offset=".8" stop-color="#c4523d"/>
        <stop offset="1" stop-color="#6d9a54"/>
      </linearGradient>
      <linearGradient id="silverSweep" x1="0" y1="0" x2="1" y2="1">
        <stop offset="0" stop-color="#f1f3f5"/>
        <stop offset="1" stop-color="#b4bbc4"/>
      </linearGradient>
      <linearGradient id="deepBlue" x1="0" y1="0" x2="0.4" y2="1">
        <stop offset="0" stop-color="#23479a"/>
        <stop offset="1" stop-color="#0b1a4a"/>
      </linearGradient>
      <linearGradient id="skyTones" x1="0" y1="0" x2="0" y2="1">
        <stop offset="0" stop-color="#8dbde0"/>
        <stop offset=".55" stop-color="#3c6fa8"/>
        <stop offset="1" stop-color="#1b2a48"/>
      </linearGradient>
    </defs>

    <rect x="0" y="200" width="665" height="400" fill="url(#silverSweep)"/>

    <path role="img" aria-label="Photo: sprinter crossing the finish line in a stadium"
          d="M0 0 H665 V290 C520 262 300 226 0 224 Z" fill="url(#stadiumTones)"/>

    <path d="M0 246 C250 250 500 330 665 520 V785 H0 Z" fill="url(#deepBlue)"/>

    <path d="M0 238 C250 242 500 322 665 512" fill="none" stroke="var(--green)" stroke-width="16"/>
    <path d="M0 249 C250 253 500 333 665 523" fill="none" stroke="var(--white)" stroke-width="3"/>

    <path role="img" aria-label="Photo: businessman opening his shirt like a hero against a blue sky"
          d="M665 340 C790 338 905 366 1030 424 V785 H665 Z" fill="url(#skyTones)"/>
    <path d="M665 322 C790 320 905 348 1030 404" fill="none" stroke="var(--green)" stroke-width="12"/>
    <path d="M665 334 C790 332 905 360 1030 416" fill="none" stroke="var(--white)" stroke-width="3"/>
  </svg>

  <header class="cover-brand">
    <div class="brand-name">Trance Guide<br>Coaching</div>
    <div class="brand-tagline">Bringing out the best in <strong>you</strong></div>
  </header>

  <article class="inside-copy">
    <h2>Lorem ipsum dolor sit</h2>
    <p>Lorem ipsum dolor sit amet, consectetuer adipiscing elit, sed diam nonummy nibh euismod tincidunt ut laoreet dolore magna aliquam erat volutpat. Ut wisi enim ad minim veniam, quis nostrud exerci tation ullamcorper suscipit lobortis nisl ut aliquip ex ea commodo consequat.</p>
    <p>Lorem ipsum dolor sit amet, consectetuer adipiscing elit, sed diam nonummy nibh euismod tincidunt ut laoreet dolore magna aliquam erat volutpat. Ut wisi enim ad minim veniam, quis nostrud exerci tation ullamcorper suscipit lobortis nisl ut aliquip ex ea commodo consequat.</p>
    <p>Lorem ipsum dolor sit amet, consectetuer adipiscing elit, sed diam nonummy nibh euismod tincidunt ut laoreet dolore magna aliquam erat volutpat. Ut wisi enim ad minim veniam, quis nostrud exerci tation ullamcorper suscipit lobortis nisl ut aliquip ex ea commodo consequat.</p>
  </article>

  <p class="panel-promise">Bringing Out<br>the Best<br>in You</p>

  <address class="contact-panel">
    <div class="brand-name">Trance Guide<br>Coaching</div>
    <div class="brand-tagline">Bringing out the best in you</div>
    <div class="contact-name">Gordon P Whitfield CLC CCH</div>
    <div class="contact-address">4629 Larkmoor Rd Ste 310<br>Albany NY 12203</div>
    <div class="contact-line">Phone <b>(518) 926-3081</b></div>
    <div class="contact-line">Fax <b>(888) 547-2263</b></div>
    <div class="contact-web">www.TranceGuideNow.example</div>
  </address>
</section>
</body>
</html>
```